Brochure Design Project

We sell and install rollout shelves for existing kitchen and bathroom cabinets. These rollout shelves are made of wood with dovetail joints. We also organize cabinets with pullouts, lazy susans, trash can pullouts, drawer organizers, and offer a selection of cabinet handles and knobs that we can also install.

Need extra days to review

```html
<!DOCTYPE html>
<html lang="en">
<head>
<meta charset="utf-8">
<title>Rollwell Brochure</title>
<link href="https://fonts.googleapis.com/css2?family=Lato:wght@400;700&family=Open+Sans:wght@400;600;700&display=swap" rel="stylesheet">
<style>
:root{
  --teal:#3fcbb0;
  --teal-soft:rgba(63,203,176,.55);
  --dark:#222426;
  --grey:#9a9c9e;
  --navy:#2b3f5c;
  --white:#ffffff;
  --ink:#111111;
}
*{margin:0;padding:0;box-sizing:border-box}
html,body{width:800px;height:1200px;overflow:hidden;background:var(--white)}
.sheet{position:absolute;left:0;top:0;width:1000px;height:1500px;transform:scale(.8);transform-origin:0 0;font-family:"Open Sans",sans-serif;color:var(--ink)}
.abs{position:absolute}
.photo{position:absolute}
.body-text{font-size:10.5px;line-height:14.6px}

/* cover panel */
.cover-bg{left:0;top:0;width:342px;height:750px;background:var(--grey)}
.cover-white{left:53px;top:0;width:255px;height:750px;background:var(--white)}
.brand{left:53px;top:50px;width:255px;height:105px;background:linear-gradient(135deg,#2f4766,#27384f)}
.brand-mark{position:absolute;left:16px;top:32px;width:24px;height:24px;border:2px solid var(--teal)}
.brand-name{position:absolute;left:55px;top:28px;font-family:"Lato",sans-serif;font-weight:700;font-size:17px;color:var(--white);letter-spacing:.5px}
.brand-tag{position:absolute;left:55px;top:48px;font-family:"Lato",sans-serif;font-size:9px;letter-spacing:1.5px;color:var(--white)}
.cover-band{left:53px;top:155px;width:255px;height:116px;background:var(--teal);padding:20px 24px;font-family:"Lato",sans-serif;font-size:21px;line-height:27px;color:var(--white)}
.cover-photo{left:53px;top:271px;width:255px;height:430px;background:linear-gradient(160deg,#3a3e44 0%,#2a2c2e 55%,#4a4a48 100%)}

/* hero */
.hero{left:342px;top:0;width:658px;height:368px;background:linear-gradient(180deg,#2e3540 0%,#56606a 45%,#3c6d7a 100%)}
.hero-band{left:342px;top:213px;width:658px;height:155px;background:var(--teal-soft)}
.hero-col{top:233px;width:240px;color:var(--white)}
.hero-col h3{font-family:"Lato",sans-serif;font-weight:400;font-size:21px;margin-bottom:6px}
.hero-col p{font-size:10.5px;line-height:14.6px}

/* contact */
.contact{left:342px;top:383px;width:325px;height:365px;background:var(--dark);color:var(--white)}
.tab{position:absolute;height:38px;padding:0 14px;font-family:"Lato",sans-serif;font-size:19px;line-height:38px;clip-path:polygon(0 0,88% 0,100% 100%,0 100%)}
.contact .tab{left:34px;top:31px;width:142px;background:#3a3d40;color:var(--white)}
.contact-item{position:absolute;left:34px;font-size:11px;line-height:15px}
.contact-item svg{display:block;margin-bottom:8px}
.contact-item b{font-weight:700}

/* about */
.about .tab{left:703px;top:412px;width:147px;background:var(--dark);color:var(--white)}
.about-text{left:703px;top:478px;width:262px}

/* welcome */
.welcome{left:0;top:760px;width:342px;height:395px;background:var(--dark);color:var(--white);padding:48px 45px}
.welcome h2{font-family:"Lato",sans-serif;font-weight:400;font-size:22px;line-height:29px;margin-bottom:24px}
.drawer-photo{left:0;top:1155px;width:342px;height:345px;background:linear-gradient(90deg,#c9cdd0 0%,#b08452 25%,#c8965f 60%,#a9794a 100%)}

/* middle */
.mid-top{left:342px;top:760px;width:325px;height:190px;background:var(--teal)}
.mid-bot{left:342px;top:1310px;width:325px;height:190px;background:var(--teal)}
.kitchen-photo{left:377px;top:847px;width:255px;height:566px;background:linear-gradient(180deg,#3b2a22 0%,#7a4a2c 35%,#8c7a68 70%,#4a3022 100%)}

/* why */
.why{left:677px;top:780px;width:303px;height:305px;background:linear-gradient(135deg,#3a4046 0%,#6a7278 60%,#a9b1b5 100%)}
.why h3{position:absolute;left:65px;top:32px;font-family:"Lato",sans-serif;font-weight:400;font-size:16px;color:var(--white)}
.why ul{list-style:none;position:absolute;left:33px;top:72px;width:255px}
.why li{display:flex;gap:13px;color:var(--white);font-size:10px;line-height:13px;margin-bottom:13px}
.why li svg{flex:none}
.why-bar{position:absolute;height:6px;background:var(--teal)}

/* services */
.service{left:709px;width:260px}
.service-head{display:flex;align-items:center;gap:16px;margin-bottom:8px}
.service-title{font-family:"Lato",sans-serif;font-size:16px;line-height:20px}
.service-title b{display:block}
</style>
</head>
<body>
<div class="sheet">

  <!-- cover -->
  <div class="abs cover-bg"></div>
  <div class="abs cover-white"></div>
  <div class="abs brand">
    <span class="brand-mark"></span>
    <span class="brand-name">ROLLWELL</span>
    <span class="brand-tag">ROLLOUT SHELVES</span>
  </div>
  <div class="abs cover-band">We Will<br>Give Your Cabinets<br>Room to Roll</div>
  <div class="photo cover-photo" role="img" aria-label="Grey trash can ready for a trash can pullout"></div>

  <!-- hero -->
  <div class="photo hero" role="img" aria-label="Bright showroom hall with an information desk"></div>
  <div class="abs hero-band"></div>
  <div class="abs hero-col" style="left:377px">
    <h3>Rollout Shelves</h3>
    <p>Solid wood rollout shelves with dovetail joints, built to fit the kitchen and bathroom cabinets you already have. Pull everything into the light instead of reaching into the back.</p>
  </div>
  <div class="abs hero-col" style="left:703px">
    <h3>Organizers</h3>
    <p>Pullouts, lazy susans, trash can pullouts and drawer organizers put every item in its place, finished with handles and knobs we supply and install.</p>
  </div>

  <!-- contact -->
  <section class="abs contact">
    <div class="tab">Contact Us</div>
    <div class="contact-item" style="top:92px">
      <svg width="22" height="22" viewBox="0 0 24 24" fill="none" stroke="#fff" stroke-width="1.8"><path d="M3 8c0-2 2-4 9-4s9 2 9 4v2h-5V8H8v2H3z"/><rect x="5" y="12" width="14" height="8" rx="1"/><circle cx="12" cy="16" r="2"/></svg>
      <b>Pho :</b> 055-210480-3316<br><b>Tel :</b> 055-210480-3316
    </div>
    <div class="contact-item" style="top:173px">
      <svg width="22" height="22" viewBox="0 0 24 24" fill="none" stroke="#fff" stroke-width="1.5"><circle cx="12" cy="12" r="10"/><ellipse cx="12" cy="12" rx="4.5" ry="10"/><path d="M2 12h20M4 7h16M4 17h16"/></svg>
      <b>Email :</b> dana.reyes@email.com<br><b>Web :</b> www.rollwell.com
    </div>
    <div class="contact-item" style="top:255px">
      <svg width="18" height="22" viewBox="0 0 18 24" fill="#fff"><path d="M9 0a8 8 0 0 0-8 8c0 6 8 16 8 16s8-10 8-16a8 8 0 0 0-8-8zm0 11a3 3 0 1 1 0-6 3 3 0 0 1 0 6z"/></svg>
      <b>Add :</b> 7112 Your Address goes here<br>Street 123, Country.
    </div>
  </section>

  <!-- about -->
  <section class="about">
    <div class="tab">ABOUT US</div>
    <p class="abs about-text body-text"><b>Rollwell</b> is a local team of cabinet organizers and installers. We started with one idea: nobody should kneel on the floor to dig through the back of a base cabinet. Today we build rollout shelves in solid wood with hand-fitted dovetail joints and full-extension slides, sized to the exact opening of your existing cabinets. We also add pullouts for spices and cleaning supplies, lazy susans for blind corners, trash can pullouts, and drawer organizers for utensils and tools. Choose cabinet handles and knobs from our range and we will install them too. One visit to measure, one visit to install, and your kitchen or bathroom works better every day.</p>
  </section>

  <!-- welcome -->
  <section class="abs welcome">
    <h2>Welcome to<br>Our Company...</h2>
    <p class="body-text">We make the cabinets you already own easier to use. Our rollout shelves are built from solid wood with dovetail joints, so they glide smoothly and hold heavy pots, pans and cleaning supplies for years. We measure every kitchen and bathroom cabinet, build each shelf to fit, and install it without replacing doors or boxes. Deep corners become lazy susans, the space under the sink becomes a trash can pullout, and cluttered drawers get custom organizers. Finish the job with new handles and knobs from our selection, fitted by the same crew.</p>
  </section>
  <div class="photo drawer-photo" role="img" aria-label="Wooden drawer organizer holding spoons and forks"></div>

  <!-- middle -->
  <div class="abs mid-top"></div>
  <div class="abs mid-bot"></div>
  <div class="photo kitchen-photo" role="img" aria-label="Kitchen with wooden cabinets and a granite island with sink"></div>

  <!-- why choose us -->
  <section class="abs why" role="img" aria-label="Bright white kitchen with organized cabinets and a plant">
    <h3>WHY CHOOSE US?</h3>
    <ul>
      <li><svg width="18" height="18" viewBox="0 0 20 20" fill="none" stroke="#3fcbb0" stroke-width="2"><circle cx="10" cy="10" r="8"/><path d="M6 10l3 3 5-6"/></svg><span>Solid wood shelves joined with real dovetails, made to last.</span></li>
      <li><svg width="18" height="18" viewBox="0 0 20 20" fill="none" stroke="#3fcbb0" stroke-width="2"><circle cx="10" cy="10" r="8"/><path d="M6 10l3 3 5-6"/></svg><span>Built to fit your existing kitchen and bath cabinets.</span></li>
      <li><svg width="18" height="18" viewBox="0 0 20 20" fill="none" stroke="#3fcbb0" stroke-width="2"><circle cx="10" cy="10" r="8"/><path d="M6 10l3 3 5-6"/></svg><span>Pullouts, lazy susans and trash can pullouts in one visit.</span></li>
      <li><svg width="18" height="18" viewBox="0 0 20 20" fill="none" stroke="#3fcbb0" stroke-width="2"><circle cx="10" cy="10" r="8"/><path d="M6 10l3 3 5-6"/></svg><span>Handles and knobs supplied and installed by our team.</span></li>
    </ul>
    <span class="why-bar" style="left:38px;top:248px;width:135px"></span>
    <span class="why-bar" style="left:73px;top:264px;width:135px"></span>
    <span class="why-bar" style="left:48px;top:280px;width:135px"></span>
  </section>

  <!-- services -->
  <div class="abs service" style="top:1098px">
    <div class="service-head">
      <svg width="40" height="44" viewBox="0 0 40 44" fill="none" stroke="#2b3f5c" stroke-width="1.5"><path d="M20 2l17 10v20L20 42 3 32V12z" stroke-dasharray="2 2"/><rect x="11" y="15" width="18" height="14"/><path d="M11 22h18M18 18.5h4M18 25.5h4"/></svg>
      <div class="service-title">Rollout<b>Shelves</b></div>
    </div>
    <p class="body-text">Solid wood shelves with dovetail joints and smooth slides, sized to each existing kitchen or bathroom cabinet.</p>
  </div>
  <div class="abs service" style="top:1220px">
    <div class="service-head">
      <svg width="40" height="44" viewBox="0 0 40 44" fill="none" stroke="#2b3f5c" stroke-width="1.5"><path d="M20 2l17 10v20L20 42 3 32V12z" stroke-dasharray="2 2"/><ellipse cx="20" cy="18" rx="9" ry="3"/><ellipse cx="20" cy="27" rx="9" ry="3"/><path d="M20 15v15"/></svg>
      <div class="service-title">Cabinet<b>Organizers</b></div>
    </div>
    <p class="body-text">Pullouts, lazy susans, trash can pullouts and drawer organizers that put every item within easy reach.</p>
  </div>
  <div class="abs service" style="top:1341px">
    <div class="service-head">
      <svg width="40" height="44" viewBox="0 0 40 44" fill="none" stroke="#2b3f5c" stroke-width="1.5"><path d="M20 2l17 10v20L20 42 3 32V12z" stroke-dasharray="2 2"/><path d="M11 20h18M13 20v4M27 20v4"/><circle cx="20" cy="28" r="2.5"/></svg>
      <div class="service-title">Handles<b>&amp; Knobs</b></div>
    </div>
    <p class="body-text">Pick cabinet handles and knobs from our selection and we fit them while we install your shelves.</p>
  </div>

</div>
</body>
</html>
```